Dean Hollis Business Card

In addition to my name design (file uploaded), black print on white card stock, e-mail address should be presented as a typical e-mail address, i.e., underlined and in blue ink, the card should include the following information:
Professor of Aviation Technology
Accident Litigation Expert Witness
Master Certificated Flight Instructor

dhollis@vexmail.example
Anchorage, Alaska
(907) 318-5074

```html
<!DOCTYPE html>
<html lang="en">
<head>
<meta charset="utf-8">
<title>Dean Hollis Business Card</title>
<link rel="stylesheet" href="https://fonts.googleapis.com/css2?family=Oswald:wght@700&family=Fira+Sans+Condensed:wght@500&display=swap">
<style>
  :root {
    --page-bg: #e6e3de;
    --card-white: #ffffff;
    --cloud-grey: #d2cfcf;
    --cloud-light: #efeeee;
    --ink: #1c1c1c;
    --mail-blue: #1f3a9c;
  }
  * { box-sizing: border-box; margin: 0; padding: 0; }
  html, body {
    width: 1200px; height: 1000px; overflow: hidden;
    background: var(--page-bg);
  }
  .canvas {
    position: relative; width: 1200px; height: 1000px;
  }
  .business-card {
    position: absolute; left: 150px; top: 243px;
    width: 900px; height: 514px;
    background: var(--card-white);
    border-radius: 34px;
    box-shadow: 0 6px 24px rgba(0,0,0,0.12);
    overflow: hidden;
  }
  .cloud-texture {
    position: absolute; inset: 0;
    background:
      radial-gradient(ellipse 340px 200px at 30% 35%, var(--cloud-light), transparent 70%),
      radial-gradient(ellipse 300px 180px at 75% 70%, var(--cloud-light), transparent 70%),
      radial-gradient(ellipse 420px 260px at 60% 30%, var(--cloud-grey), transparent 75%),
      radial-gradient(ellipse 380px 240px at 20% 80%, var(--cloud-grey), transparent 75%),
      linear-gradient(135deg, #e4e2e2, #d8d6d6);
  }
  .card-frame {
    position: absolute; inset: 18px;
    border: 2px solid var(--ink);
    border-radius: 26px;
  }
  .card-name {
    position: absolute; left: 52px; top: 26px;
    font-family: "Oswald", sans-serif; font-weight: 700;
    font-size: 116px; line-height: 1.1; letter-spacing: 1px;
    color: var(--ink); text-transform: uppercase; white-space: nowrap;
  }
  .credentials {
    position: absolute; left: 250px; top: 205px;
    list-style: none;
    font-family: "Fira Sans Condensed", sans-serif; font-weight: 500;
    font-size: 34px; line-height: 50px; color: var(--ink);
  }
  .credentials li { display: flex; align-items: center; gap: 8px; }
  .tick { width: 18px; height: 18px; }
  .contact-row {
    position: absolute; left: 52px; right: 52px; bottom: 42px;
    display: flex; justify-content: space-between; align-items: center;
    font-family: "Fira Sans Condensed", sans-serif; font-weight: 500;
    font-size: 24px; color: var(--ink);
  }
  .contact-item { display: flex; align-items: center; gap: 8px; }
  .contact-icon { width: 20px; height: 20px; }
  .contact-email {
    color: var(--mail-blue); text-decoration: underline;
  }
</style>
</head>
<body>
<main class="canvas">
  <section class="business-card">
    <div class="cloud-texture" role="img" aria-label="Soft grey cloudy sky texture"></div>
    <div class="card-frame"></div>
    <h1 class="card-name">Dean E. Hollis</h1>
    <ul class="credentials">
      <li>Professor of Aviation Technology
        <svg class="tick" viewBox="0 0 20 20"><path d="M3 10 L8 15 L17 4" fill="none" stroke="#1c1c1c" stroke-width="3"/></svg></li>
      <li>Accident Litigation Expert Witness
        <svg class="tick" viewBox="0 0 20 20"><path d="M3 10 L8 15 L17 4" fill="none" stroke="#1c1c1c" stroke-width="3"/></svg></li>
      <li>Master Certificated Flight Instructor
        <svg class="tick" viewBox="0 0 20 20"><path d="M3 10 L8 15 L17 4" fill="none" stroke="#1c1c1c" stroke-width="3"/></svg></li>
    </ul>
    <div class="contact-row">
      <span class="contact-item">
        <svg class="contact-icon" viewBox="0 0 20 20"><path d="M3 6 Q10 1 17 6 L15 9 L12 7 L8 7 L5 9 Z M5 10 H15 V17 H5 Z" fill="#1c1c1c"/><circle cx="10" cy="13.5" r="2" fill="#fff"/></svg>
        (907) 318-5074
      </span>
      <span class="contact-item">
        <svg class="contact-icon" viewBox="0 0 20 20"><rect x="2" y="4" width="16" height="12" fill="#1c1c1c"/><path d="M2 4 L10 11 L18 4" fill="none" stroke="#fff" stroke-width="1.5"/></svg>
        <span class="contact-email">dhollis@vexmail.example</span>
      </span>
      <span class="contact-item">
        <svg class="contact-icon" viewBox="0 0 20 20"><path d="M10 1 C5 1 3 5 3 8 C3 13 10 19 10 19 C10 19 17 13 17 8 C17 5 15 1 10 1 Z" fill="#1c1c1c"/><circle cx="10" cy="8" r="3" fill="#fff"/></svg>
        Anchorage, Alaska
      </span>
    </div>
  </section>
</main>
</body>
</html>
```